TELVIRA Web Page

We need a corporate web site for a new company TELVIRA Corporation. TELVIRA is a technology company that has developed a new virtualization solution for corporate applications. Our target customers are IT professionals. We have a logo, which we will provide.

Final design should communicate: innovation, stability, professionalism

Industry/Entity Type

It Company

```html
<!DOCTYPE html>
<html lang="en">
<head>
<meta charset="utf-8">
<title>TELVIRA – Virtualization Solution for IT Professionals</title>
<link href="https://fonts.googleapis.com/css2?family=Oswald:wght@300;500;700&family=Questrial&family=Arimo:wght@400;700&display=swap" rel="stylesheet">
<style>
:root{
  --blue:#0b7bb8;
  --blue-dark:#06649a;
  --blue-text:#1589c4;
  --green:#9fc21f;
  --green-dark:#86a913;
  --lime:#b6cd24;
  --ink:#222;
  --muted:#555;
  --white:#fff;
}
*{margin:0;padding:0;box-sizing:border-box}
html,body{width:784px;height:1200px;overflow:hidden;background:var(--white)}
body{position:relative;font-family:Arimo,Arial,sans-serif;color:var(--ink)}
.abs{position:absolute}

/* header */
.site-header{left:0;top:0;width:784px;height:86px;background:var(--blue);border-bottom:5px solid var(--blue-dark)}
.brand{left:12px;top:7px;width:132px;height:68px;border-radius:50%;background:var(--white);box-shadow:0 2px 4px rgba(0,0,0,.3);display:flex;align-items:center;justify-content:center;font-family:Arimo,Arial,sans-serif;font-weight:700;font-size:19px;color:var(--blue-dark);letter-spacing:.5px}
.tagline{left:230px;top:30px;width:320px;text-align:center;font-family:Oswald,sans-serif;font-weight:300;font-size:20px;color:var(--white)}
.tagline b{font-weight:700}
.call-label{right:17px;top:15px;font-family:Arimo,Arial,sans-serif;font-size:14px;color:var(--white)}
.call-number{right:17px;top:32px;display:flex;align-items:center;gap:6px;font-family:Oswald,sans-serif;font-weight:300;font-size:26px;color:var(--white)}

/* nav */
.main-nav{left:0;top:86px;width:784px;height:33px;background:linear-gradient(var(--green),var(--green-dark));display:flex;padding-left:10px}
.main-nav a{font-family:Arimo,Arial,sans-serif;font-size:12.5px;color:var(--white);text-decoration:none;height:33px;line-height:33px;text-align:center}
.main-nav a.active{background:var(--blue)}

/* hero */
.hero{left:0;top:119px;width:784px;height:305px;background:radial-gradient(circle at 75% 35%,#e8f0f4 0,#9fb4c2 30%,#4f6372 65%,#26323c 100%)}
.hero-copy{left:32px;top:186px;width:295px;font-size:11px;line-height:13.5px;color:#111}
.quote-btn{left:31px;top:266px;width:196px;height:31px;border-radius:6px;background:linear-gradient(#9fd26a,#6fb23a);border:2px solid #b8e08c;font-family:Oswald,sans-serif;font-weight:500;font-size:18px;color:var(--white);padding-left:22px;line-height:27px;letter-spacing:.5px}

/* why */
.section-title{font-family:Questrial,sans-serif;font-size:30px;color:var(--blue-text)}
.why-copy{left:22px;top:502px;width:400px;font-size:9.2px;line-height:11.6px;color:var(--ink)}
.why-list{left:33px;top:572px;list-style:none}
.why-list li{display:flex;align-items:center;gap:11px;height:20.2px;font-size:9.4px;color:#111}

/* news */
.news-item{left:528px;width:212px;height:88px;border-bottom:1px dotted #999}
.news-date{position:absolute;left:2px;top:0;width:26px;text-align:center}
.news-date .day{width:26px;height:26px;border-radius:50%;background:var(--blue-text);border:2px solid #cfe4f0;color:var(--white);font-family:Oswald,sans-serif;font-size:14px;line-height:22px}
.news-date .month{font-size:9.5px;font-weight:700;color:var(--blue-text);margin-top:5px}
.news-body{position:absolute;left:48px;top:0;width:165px}
.news-body h4{font-size:9.6px;font-weight:700;color:#222;margin-bottom:4px}
.news-body p{font-size:8.4px;line-height:10.5px;color:var(--muted)}
.more{font-size:8.4px;font-weight:700;color:var(--green-dark);text-decoration:none}
.news-more{left:683px;top:669px;font-size:9px;color:var(--green-dark)}

/* features */
.feature{width:210px}
.feature-icon{width:90px;height:70px;position:relative}
.feature-icon .back{position:absolute;left:20px;top:0;width:68px;height:68px;border-radius:50%;background:var(--lime)}
.feature-icon .front{position:absolute;left:0;top:0;width:68px;height:68px;border-radius:50%;background:var(--blue);border:2px solid var(--white);display:flex;align-items:center;justify-content:center}
.feature h3{font-family:Arimo,Arial,sans-serif;font-weight:700;font-size:14.5px;color:var(--blue-text);margin:12px 0 8px 0}
.feature p{font-size:9.2px;line-height:11.6px;color:var(--muted);width:205px}
.feature .more{display:block;margin-top:6px;color:#555}

/* partners */
.partners{left:0;top:980px;width:784px;height:86px;box-shadow:0 -8px 12px -10px rgba(0,0,0,.15),0 8px 12px -10px rgba(0,0,0,.15)}
.partner-row{left:40px;top:995px;width:704px;height:56px;display:flex;align-items:center;justify-content:space-between}
.partner{display:flex;align-items:center;gap:5px;font-family:Arimo,Arial,sans-serif;font-weight:700;font-size:15px;color:#4a4a4a}
.partner .mark{width:14px;height:14px;border-radius:50%;background:var(--blue-text)}
.partner .sq{width:14px;height:14px;background:var(--green)}
.arrow{font-family:Questrial,sans-serif;font-size:34px;color:#777;top:998px}

/* footer */
.site-footer{left:0;top:1105px;width:784px;height:95px;background:var(--blue)}
.social{left:327px;top:1120px;display:flex;gap:8px}
.social span{width:20px;height:20px;border-radius:50%;background:var(--white)}
.footer-nav{left:0;top:1162px;width:784px;text-align:center;font-size:9.6px}
.footer-nav a{color:#e6f04a;text-decoration:none;margin:0 2px}
.copyright{left:0;top:1179px;width:784px;text-align:center;font-size:8px;color:#8cc2e2}
</style>
</head>
<body>

<header class="site-header abs"></header>
<div class="brand abs">TELVIRA</div>
<div class="tagline abs">Virtualization Solution for <b>IT Professionals</b></div>
<div class="call-label abs">Toll free call now!</div>
<div class="call-number abs">
  <svg width="26" height="26" viewBox="0 0 26 26" aria-hidden="true"><circle cx="13" cy="13" r="11.5" fill="none" stroke="#fff" stroke-width="1.6"/><path d="M9 7.5c-1 .6-1.6 1.6-1.2 3 .8 3 3.8 6.6 6.8 7.6 1.4.4 2.4 0 3-1l-2-2-1.5.8c-1.3-.6-3-2.4-3.6-3.7l.8-1.5z" fill="#fff"/></svg>
  0800 555 0142
</div>

<nav class="main-nav abs">
  <a class="active" href="#" style="width:85px">Home</a>
  <a href="#" style="width:135px">Services</a>
  <a href="#" style="width:110px">Solutions</a>
  <a href="#" style="width:125px">Partners</a>
  <a href="#" style="width:110px">About Us</a>
  <a href="#" style="width:120px">Contact</a>
</nav>

<div class="hero abs" role="img" aria-label="Businessman touching a glowing cloud icon linked to a network of nodes"></div>
<p class="hero-copy abs">Lorem ipsum dolor sit amet, consectetur adipisicing elit, sed do eiusmod tempor incididunt ut labore et dolore magna aliqua. Ut enim ad minim veniam, quis nostrud exercitation ullamco laboris nisi ut aliquip ex ea commodo consequat.</p>
<div class="quote-btn abs">REQUEST A QUOTE</div>

<h2 class="section-title abs" style="left:23px;top:446px">Why TELVIRA</h2>
<p class="why-copy abs">Lorem ipsum dolor sit amet, consectetur adipisicing elit, sed do eiusmod tempor incididunt ut l abore et dolore magna aliqua. Ut enim ad minim veniam, quis nostrud exercitation ullamco laboris nisi ut aliquip ex ea commodo consequat. Duis aute irure dolor in reprehenderit in voluptate velit esse cillum dolore eu fugiat nulla pariatur. Excepteur sint occaecat cupidatat non proident, sunt in culpa qui officia deserunt mollit anim id est laborum.</p>
<ul class="why-list abs">
  <li><svg width="13" height="13" viewBox="0 0 13 13" aria-hidden="true"><circle cx="6" cy="7" r="5.5" fill="#2c3a2c"/><path d="M3 6.5l2.5 2.5L12 1.5" fill="none" stroke="#6cbf2a" stroke-width="2.2"/></svg>Sed ut perspiciatis, unde omnis iste natus error sit voluptatem accusantium</li>
  <li><svg width="13" height="13" viewBox="0 0 13 13" aria-hidden="true"><circle cx="6" cy="7" r="5.5" fill="#2c3a2c"/><path d="M3 6.5l2.5 2.5L12 1.5" fill="none" stroke="#6cbf2a" stroke-width="2.2"/></svg>Doloremque laudantium, totam rem aperiam eaque ipsa, quae ab illo inventore</li>
  <li><svg width="13" height="13" viewBox="0 0 13 13" aria-hidden="true"><circle cx="6" cy="7" r="5.5" fill="#2c3a2c"/><path d="M3 6.5l2.5 2.5L12 1.5" fill="none" stroke="#6cbf2a" stroke-width="2.2"/></svg>Veritatis et quasi architecto beatae vitae dicta sunt, explicabo.</li>
  <li><svg width="13" height="13" viewBox="0 0 13 13" aria-hidden="true"><circle cx="6" cy="7" r="5.5" fill="#2c3a2c"/><path d="M3 6.5l2.5 2.5L12 1.5" fill="none" stroke="#6cbf2a" stroke-width="2.2"/></svg>Nemo enim ipsam voluptatem, quia voluptas sit, aspernatur aut odit aut fugit</li>
  <li><svg width="13" height="13" viewBox="0 0 13 13" aria-hidden="true"><circle cx="6" cy="7" r="5.5" fill="#2c3a2c"/><path d="M3 6.5l2.5 2.5L12 1.5" fill="none" stroke="#6cbf2a" stroke-width="2.2"/></svg>Quia consequuntur magni dolores eos, qui ratione voluptatem sequi nesciunt</li>
</ul>

<h2 class="section-title abs" style="left:528px;top:449px">Latest News</h2>
<article class="news-item abs" style="top:502px">
  <div class="news-date"><div class="day">07</div><div class="month">AUG</div></div>
  <div class="news-body"><h4>Lorem ipsum dolor sit amet</h4><p>Lorem ipsum dolor sit amet, consectetur adipisicing elit, sed do.</p><a class="more" href="#">read more +</a></div>
</article>
<article class="news-item abs" style="top:590px">
  <div class="news-date"><div class="day">07</div><div class="month">AUG</div></div>
  <div class="news-body"><h4>Lorem ipsum dolor sit amet</h4><p>Lorem ipsum dolor sit amet, consectetur adipisicing elit, sed do.</p><a class="more" href="#">read more +</a></div>
</article>
<a class="news-more abs" href="#">more news +</a>

<section class="feature abs" style="left:31px;top:750px">
  <div class="feature-icon"><span class="back"></span><span class="front">
    <svg width="40" height="36" viewBox="0 0 40 36" aria-hidden="true"><path d="M10 20a7 7 0 0 1 2-13.7A10 10 0 0 1 30 8a6 6 0 0 1 1 12z" fill="#fff"/><path d="M12 25q8 6 16 0M15 29q5 3 10 0" fill="none" stroke="#fff" stroke-width="2"/></svg>
  </span></div>
  <h3>At Vero Eos Et</h3>
  <p>Xos et accusamus et iusto odio dignissimos ducimus, qui blanditiis praesentium voluptatum deleniti atque corrupti, quos dolores et quas molestias excepturi</p>
  <a class="more" href="#">read more +</a>
</section>
<section class="feature abs" style="left:287px;top:750px">
  <div class="feature-icon"><span class="back"></span><span class="front">
    <svg width="40" height="30" viewBox="0 0 40 30" aria-hidden="true"><rect x="8" y="3" width="24" height="17" rx="2" fill="#fff"/><rect x="4" y="22" width="32" height="4" rx="1" fill="#fff"/></svg>
  </span></div>
  <h3>IT Accusamus Et Iusto</h3>
  <p>Et harum quidem rerum facilis est et expedita distinctio. Nam libero tempore, cum soluta nobis est eligendi optio, cumque nihil impedit, quo minus id, quod maxime placeat, facere</p>
  <a class="more" href="#">read more +</a>
</section>
<section class="feature abs" style="left:543px;top:750px">
  <div class="feature-icon"><span class="back"></span><span class="front">
    <svg width="40" height="36" viewBox="0 0 40 36" aria-hidden="true"><circle cx="20" cy="11" r="7" fill="#fff"/><path d="M7 32q0-12 13-12t13 12z" fill="#fff"/></svg>
  </span></div>
  <h3>Dignissimos Ducimus</h3>
  <p>qui dolorem ipsum, quia dolor sit amet, conse adipisci[ng] velit, sed quia non numquam [do] modi tempora inci[di]dunt, ut labore et dolore magnam aliquam quaerat voluptatem.</p>
  <a class="more" href="#">read more +</a>
</section>

<div class="partners abs"></div>
<span class="arrow abs" style="left:6px">‹</span>
<span class="arrow abs" style="right:8px">›</span>
<div class="partner-row abs">
  <span class="partner"><span class="mark"></span>Norvale</span>
  <span class="partner">Quentis</span>
  <span class="partner">Datalume</span>
  <span class="partner"><span class="sq"></span>Paybridge</span>
  <span class="partner">Voltara</span>
  <span class="partner"><span class="mark"></span>Scientia</span>
  <span class="partner">Corvane</span>
</div>

<footer class="site-footer abs"></footer>
<div class="social abs" aria-label="Social links"><span></span><span></span><span></span><span></span><span></span></div>
<nav class="footer-nav abs"><a href="#">Home</a> <a href="#">Services</a> <a href="#">Solutions</a> <a href="#">Partners</a> <a href="#">About Us</a> <a href="#">Contact</a></nav>
<p class="copyright abs">© Copyright 2013 TELVIRA. All Rights Reserved</p>

</body>
</html>
```